DEAN COLLOPY PROPERTY SERVICES

I want a business card that is clean and simple.
'Dean Collopy Property Services' is the title.
Somewhere on the card needs to be 'Carpentry, Tiling, painting and garden services'

On the back of card
PH 087 394 1526
email: deancollopypropertyservices@fernmail.net

I have attached a picture of my other business. I would like the font and design to be similar to the bathroom business.

Many thanks.

```html
<!DOCTYPE html>
<html lang="en">
<head>
<meta charset="utf-8">
<title>Dean Collopy Property Services – Business Card</title>
<link rel="stylesheet" href="https://fonts.googleapis.com/css2?family=Montserrat:wght@400;500;600;700&display=swap">
<style>
  :root {
    --page-bg: #e9e9e9;
    --card-bg: #ffffff;
    --ink: #111111;
    --shadow: rgba(0, 0, 0, 0.18);
  }
  * { box-sizing: border-box; margin: 0; padding: 0; }
  html, body {
    width: 1200px;
    height: 800px;
    overflow: hidden;
    background: var(--page-bg);
    font-family: "Montserrat", sans-serif;
    color: var(--ink);
  }
  .canvas {
    width: 1200px;
    height: 800px;
    display: flex;
    flex-direction: column;
    align-items: center;
    justify-content: center;
    gap: 40px;
  }
  .card {
    position: relative;
    width: 600px;
    height: 340px;
    background: var(--card-bg);
    box-shadow: 0 12px 30px var(--shadow);
  }

  /* Front */
  .brand {
    position: absolute;
    top: 82px;
    left: 0;
    right: 0;
    text-align: center;
  }
  .brand-name {
    font-size: 62px;
    font-weight: 500;
    letter-spacing: 0.01em;
    line-height: 1;
  }
  .brand-sub {
    margin-top: 4px;
    font-size: 21px;
    font-weight: 400;
    letter-spacing: 0.32em;
    line-height: 1;
    padding-left: 40px;
  }
  .services {
    position: absolute;
    left: 28px;
    bottom: 22px;
    font-size: 21px;
    font-weight: 400;
    letter-spacing: 0.01em;
  }

  /* Back */
  .phone {
    position: absolute;
    top: 104px;
    left: 0;
    right: 0;
    display: flex;
    align-items: center;
    justify-content: center;
    gap: 20px;
  }
  .phone-number {
    font-size: 34px;
    font-weight: 700;
    letter-spacing: 0.18em;
  }
  .icon {
    flex: none;
    display: block;
  }
  .email {
    position: absolute;
    left: 28px;
    bottom: 24px;
    display: flex;
    align-items: center;
    gap: 12px;
  }
  .email-address {
    font-size: 19px;
    font-weight: 400;
  }
</style>
</head>
<body>
<main class="canvas">

  <section class="card card-front" aria-label="Card front">
    <div class="brand">
      <h1 class="brand-name">Dean Collopy</h1>
      <p class="brand-sub">PROPERTY SERVICES</p>
    </div>
    <p class="services">Carpentry, Tiling, painting and garden services</p>
  </section>

  <section class="card card-back" aria-label="Card back">
    <div class="phone">
      <svg class="icon icon-phone" width="46" height="46" viewBox="0 0 46 46" aria-hidden="true">
        <circle cx="23" cy="23" r="23" fill="var(--ink)"/>
        <path d="M15 12c1.5-1 3-.6 3.7.6l2.2 3.8c.6 1 .3 2.2-.6 2.9l-1.6 1.2c1.2 2.7 3.4 4.9 6.1 6.1l1.2-1.6c.7-.9 1.9-1.2 2.9-.6l3.8 2.2c1.2.7 1.6 2.2.6 3.7l-1.3 1.9c-.9 1.3-2.6 1.9-4.1 1.4C20.8 33.4 13.6 26.2 11.4 19c-.5-1.5.1-3.2 1.4-4.1z" fill="var(--card-bg)"/>
      </svg>
      <span class="phone-number">087 394 1526</span>
    </div>
    <div class="email">
      <svg class="icon icon-mail" width="36" height="36" viewBox="0 0 36 36" aria-hidden="true">
        <circle cx="18" cy="18" r="18" fill="var(--ink)"/>
        <rect x="9" y="12" width="18" height="12" fill="none" stroke="var(--card-bg)" stroke-width="1.8"/>
        <path d="M9 12l9 7 9-7M9 24l6.5-6M27 24l-6.5-6" fill="none" stroke="var(--card-bg)" stroke-width="1.6"/>
      </svg>
      <span class="email-address">deancollopypropertyservices@fernmail.net</span>
    </div>
  </section>

</main>
</body>
</html>
```